Mediation service showing compassion, collaboration, and resolution

I would like to purchase a customized version of a design you have previously submitted - https://www.pixelbidhub.com/design/48172635

Hello,

I would like a design for a flyer for my mediation business.
I also want to include a message that says that I offer rates on sliding scale.
My website is: www.morvantelkresolve.com

Let me know what other details you might want?

Thank you,

Teodric

Target Market(s)

Local community, western Massachusetts USA. Businesses, families, individuals.

Industry/Entity Type

Mediation, Legal, Alternative Dispute Resolution, Divorce, Unions

Font styles to use
Sans Serif

Colors
0094D4
00A9DD
6FCCEA
C7EBF8
E9F6FB
00AB8E
00BBA5
67D7C9
C6EFE9
E9F9F6

Requirements
Must have
• “Sliding scale rates available “. Phone and email details. +1.555.384.7290 and email: teodric@morvantelkresolve.com as well as we code to my website www.morvantelkresolve.com

```html
<!DOCTYPE html>
<html lang="en">
<head>
<meta charset="utf-8">
<title>Teodric F. Morvantelk – Alternative Dispute Resolution</title>
<link href="https://fonts.googleapis.com/css2?family=Barlow:wght@400;500;600&family=Poppins:wght@600;700&display=swap" rel="stylesheet">
<style>
  :root{
    --teal-deep:#176a7e;
    --teal-mid:#27a6a6;
    --teal-soft:#4cc9c3;
    --aqua:#45d6d6;
    --aqua-bright:#5ddfe0;
    --aqua-pale:#c9f4f4;
    --aqua-mist:#e3fafa;
    --tick:#1b9aa0;
    --band:#f1f1f1;
    --ink:#1d2b2e;
    --white:#ffffff;
  }
  *{margin:0;padding:0;box-sizing:border-box}
  html,body{width:927px;height:1200px;overflow:hidden;background:var(--white)}
  .flyer{position:relative;width:927px;height:1200px;overflow:hidden;background:var(--white);font-family:"Barlow",sans-serif;color:var(--ink)}
  .backdrop{position:absolute;inset:0}

  .intro{position:absolute;left:55px;top:58px;width:366px;color:var(--white)}
  .intro__title{font-family:"Poppins",sans-serif;font-weight:700;font-size:36px;line-height:1.1;letter-spacing:-0.3px;margin-bottom:14px}
  .intro__text{font-size:13.6px;line-height:18.2px;text-align:justify;margin-bottom:9px}

  .brand{position:absolute;left:500px;top:32px;width:414px;text-align:center}
  .brand__name{font-family:"Barlow",sans-serif;font-weight:500;font-size:34px;color:#111;letter-spacing:0.5px;line-height:1.2}
  .brand__tag{font-family:"Poppins",sans-serif;font-weight:600;font-size:10.5px;color:#111;margin-top:6px;letter-spacing:0.3px}

  .portrait{position:absolute;left:513px;top:161px;width:312px;height:312px;border-radius:50%;background:var(--aqua);padding:12px}
  .portrait__photo{width:100%;height:100%;border-radius:50%;
    background:radial-gradient(circle at 50% 45%,#c68f75 0 26%,transparent 27%),
               radial-gradient(ellipse at 55% 95%,#c8464a 0 34%,transparent 35%),
               linear-gradient(180deg,#7f8689,#5d6568)}

  .scene{position:absolute;left:14px;top:517px;width:492px;height:397px}

  .provide{position:absolute;left:521px;top:540px;width:300px;height:56px;border-radius:28px;background:var(--aqua);
    display:flex;align-items:center;justify-content:center;font-family:"Poppins",sans-serif;font-weight:700;font-size:33px;color:var(--white);letter-spacing:1px}

  .services{position:absolute;left:483px;top:612px;width:444px;list-style:none}
  .services li{display:flex;align-items:center;padding-left:42px;padding-right:20px;font-size:17.2px;line-height:20px;position:relative;letter-spacing:0.2px}
  .services li::before{content:"";position:absolute;left:42px;top:50%;width:7px;height:4px;border-left:2px solid var(--tick);border-bottom:2px solid var(--tick);transform:translate(-14px,-70%) rotate(-45deg)}
  .services li span{display:block;padding-left:4px}
  .services li.shaded{background:var(--band)}

  .contact{position:absolute;left:40px;top:984px;list-style:none}
  .contact li{display:flex;align-items:flex-start;font-size:16.4px;line-height:19px;margin-bottom:14.5px;color:var(--ink)}
  .contact svg{width:22px;height:22px;flex:none;margin-right:10px;fill:var(--tick)}
</style>
</head>
<body>
<main class="flyer">
  <svg class="backdrop" viewBox="0 0 927 1200" aria-hidden="true">
    <defs>
      <linearGradient id="teal-wash" x1="0" y1="0" x2="1" y2="1">
        <stop offset="0" stop-color="#176a7e"/>
        <stop offset="0.45" stop-color="#27a6a6"/>
        <stop offset="1" stop-color="#55cfc8"/>
      </linearGradient>
    </defs>
    <path d="M0 0H927V600C860 540 770 530 650 510C520 488 430 395 300 404C170 414 60 468 0 526Z" fill="url(#teal-wash)"/>
    <path d="M0 526C60 468 170 414 300 404C430 395 520 488 650 510C770 530 860 540 927 600V625C860 565 770 550 650 528C520 506 430 420 300 430C170 440 60 490 0 545Z" fill="#3fd2d2" opacity="0.9"/>
    <path d="M0 0V0" fill="none"/>
    <path d="M455 0H927V176C870 190 800 168 740 150C660 126 580 162 512 132C462 108 448 40 465 0Z" fill="#46d4d4"/>
    <path d="M470 0H927V160C862 172 790 150 730 138C650 122 575 150 510 118C468 95 462 35 478 0Z" fill="#ffffff"/>
    <circle cx="532" cy="288" r="58" fill="#ffffff" opacity="0.08"/>
    <circle cx="760" cy="440" r="42" fill="#ffffff" opacity="0.1"/>
    <path d="M0 920C100 898 240 880 315 955C362 1005 330 1100 352 1200H0Z" fill="var(--aqua-pale)"/>
    <path d="M0 880C90 870 210 860 300 930" fill="none" stroke="#ffffff" stroke-width="2"/>
    <path d="M340 1200C450 1158 600 1168 700 1180C800 1188 880 1162 927 1150V1200Z" fill="var(--aqua-pale)"/>
    <g fill="none" stroke="#bfeeee" stroke-width="1.6">
      <circle cx="16" cy="895" r="12"/><circle cx="49" cy="876" r="7"/>
      <circle cx="307" cy="1038" r="12"/><circle cx="722" cy="1172" r="7"/>
      <circle cx="529" cy="532" r="5"/><circle cx="843" cy="557" r="5"/><circle cx="815" cy="600" r="5"/><circle cx="497" cy="581" r="5"/>
    </g>
  </svg>

  <section class="intro">
    <h1 class="intro__title">What is Mediation?</h1>
    <p class="intro__text">Mediation is a form of facilitated negotiation, by a mediator, who helps the parties engage in a dialog to search for a joint agreement. All decisions, from agree­ing to participate in the mediation, to possible terms of an agreement, are decided by the parties.</p>
    <p class="intro__text">The mediator has no authority over the parties nor impose any directives. The mediator is there to help the parties find their interests, list and organize the options they have vs the alternatives and the outcome probabili­ties for each outside a resolution via the mediation process.</p>
  </section>

  <header class="brand">
    <div class="brand__name">Teodric F. Morvantelk</div>
    <div class="brand__tag">Alternative Dispute Resolution</div>
  </header>

  <div class="portrait">
    <div class="portrait__photo" role="img" aria-label="Portrait photo of the mediator in a red shirt against a grey wall"></div>
  </div>

  <svg class="scene" viewBox="0 0 492 397" role="img" aria-label="Line illustration of a mediator with a notepad talking with a client, both seated on benches beside a potted plant">
    <path d="M70 130C80 80 180 65 300 60C380 56 410 90 400 150C390 220 300 250 200 255C100 260 60 190 70 130Z" fill="#c9f4f4"/>
    <path d="M10 300C15 250 70 230 130 250C200 275 260 210 340 195C420 180 495 220 490 290C485 360 400 395 280 395C150 395 5 370 10 300Z" fill="#5ddfe0"/>
  </svg>

  <div class="provide">WE PROVIDE</div>

  <ul class="services">
    <li style="height:56px"><span>Divorce &amp; Family Mediation (Sliding scale rates)</span></li>
    <li class="shaded" style="height:30px"><span>Commercial &amp; business related Mediation</span></li>
    <li style="height:61px"><span>Mediation between dealer, agent, distributor &amp; supplier, manufacturer</span></li>
    <li class="shaded" style="height:29px"><span>Employment contract negotiations</span></li>
    <li style="height:43px"><span>Mediation via videoconference</span></li>
    <li class="shaded" style="height:30px"><span>Ombuds contracting</span></li>
    <li style="height:64px"><span>International business &amp; trading conflict mediation</span></li>
    <li class="shaded" style="height:51px"><span>Merger Negotiations and Business Collaboration</span></li>
    <li style="height:34px"><span>Contract negotiation consultancy</span></li>
    <li class="shaded" style="height:29px"><span>Mediation for property or entity division</span></li>
    <li style="height:41px"><span>Mediation Coaching</span></li>
    <li class="shaded" style="height:30px"><span>Workplace Mediation</span></li>
    <li style="height:30px"><span>Meetings Facilitation</span></li>
  </ul>

  <ul class="contact">
    <li><svg viewBox="0 0 24 24" aria-hidden="true"><path d="M6.6 10.8a15.1 15.1 0 0 0 6.6 6.6l2.2-2.2c.3-.3.7-.4 1-.2 1.1.4 2.3.6 3.6.6.6 0 1 .4 1 1V20c0 .6-.4 1-1 1A17 17 0 0 1 3 4c0-.6.4-1 1-1h3.5c.6 0 1 .4 1 1 0 1.3.2 2.5.6 3.6.1.3 0 .7-.2 1z"/></svg>+1.555.384.7290</li>
    <li><svg viewBox="0 0 24 24" aria-hidden="true"><path d="M2 5h20v14H2z" opacity=".9"/><path d="M2 5l10 7 10-7" fill="none" stroke="#c9f4f4" stroke-width="1.6"/></svg>teodric@morvantelkresolve.com</li>
    <li><svg viewBox="0 0 24 24" aria-hidden="true"><circle cx="12" cy="12" r="10"/><path d="M2 12h20M12 2c3 3 3 17 0 20M12 2c-3 3-3 17 0 20M4 7h16M4 17h16" fill="none" stroke="#c9f4f4" stroke-width="1.4"/></svg>www.morvantelkresolve.com</li>
    <li><svg viewBox="0 0 24 24" aria-hidden="true"><path d="M12 2a7 7 0 0 0-7 7c0 5 7 13 7 13s7-8 7-13a7 7 0 0 0-7-7zm0 9.5A2.5 2.5 0 1 1 12 6.5a2.5 2.5 0 0 1 0 5z"/></svg><span>82 Linden Crest Road #410,<br>Harlow MA 01999 USA</span></li>
  </ul>
</main>
</body>
</html>
```